Tolvane Logo & Packaging Design

I need a logo and packaging label for a roll-on deodorant. I have a design in mind, however it needs to be changed to suit the information based in the design brief.

The logo and product label should be a point of differentiation, to help the brand stand out from the masses.

I have attached a detailed brief with all required information, so please review carefully.

Target Market(s)

Modern man working professional, 24-35, $70K+ income, stays fit and healthy

Industry/Entity Type

Hair And Beauty

Requirements
Must have
• colour, bold typeface, logo and graphic.
• please see this landing page for idea reference: http://www.kestrelhopworks.com/our-ales/
• https://static1.pinwellmedia.com/static/71ac9d02f3c19bab47d20c38/t/6b293f5635b705217c4e1bc9/1622645315366/QRT
• https://static1.pinwellmedia.com/static/71ac9d02f3c19bab47d20c38/t/706808d47b5a74ed79d3e4a0/1509023834683/?format=750w
Should not have
• no black and white only.

```html
<!DOCTYPE html>
<html lang="en">
<head>
<meta charset="utf-8">
<title>Tolvane Roll-On Deodorant Label</title>
<link rel="stylesheet" href="https://fonts.googleapis.com/css2?family=Cinzel:wght@400;700&display=swap">
<style>
  :root {
    --backdrop: #2a80dc;
    --label-base: #e9e9ea;
    --label-light: #f5f5f5;
    --navy: #1f2e8f;
    --white: #ffffff;
    --wave-blue: #9fcbea;
    --wave-pale: #dbe9f3;
  }
  * { margin: 0; padding: 0; box-sizing: border-box; }
  html, body {
    width: 1200px;
    height: 1200px;
    overflow: hidden;
    background: var(--backdrop);
  }
  .canvas {
    position: relative;
    width: 1200px;
    height: 1200px;
  }
  .label {
    position: absolute;
    left: 306px;
    top: 61px;
    width: 588px;
    height: 1078px;
    border-radius: 0 0 36px 36px;
    background: linear-gradient(90deg, var(--label-base) 0%, var(--label-light) 45%, var(--label-base) 100%);
    overflow: hidden;
    font-family: "Cinzel", serif;
    color: var(--navy);
    text-align: center;
  }
  .label__wave-area {
    position: absolute;
    inset: 0;
    width: 100%;
    height: 100%;
  }
  .brand-box {
    position: absolute;
    left: 76px;
    top: 150px;
    width: 440px;
    height: 112px;
    background: var(--navy);
    padding: 7px;
  }
  .brand-box__frame {
    width: 100%;
    height: 100%;
    border: 2px solid var(--white);
    display: flex;
    align-items: center;
    justify-content: center;
  }
  .brand-name {
    font-size: 62px;
    font-weight: 700;
    letter-spacing: 4px;
    line-height: 1;
    color: var(--white);
  }
  .product-title {
    font-weight: 400;
  }
  .product-title__line {
    position: absolute;
    left: 0;
    right: 0;
    font-size: 48px;
    letter-spacing: 3px;
    line-height: 60px;
  }
  .product-title__line--first { top: 334px; }
  .product-title__line--second { top: 396px; }
  .product-title__line--range { top: 544px; }
  .product-title__joiner {
    position: absolute;
    left: 0;
    right: 0;
    top: 476px;
    font-size: 26px;
    letter-spacing: 2px;
    line-height: 34px;
  }
  .volume-pill {
    position: absolute;
    left: 228px;
    top: 1012px;
    width: 133px;
    height: 40px;
    border-radius: 20px;
    background: var(--navy);
    color: var(--white);
    font-size: 20px;
    line-height: 40px;
    letter-spacing: 1px;
  }
</style>
</head>
<body>
  <main class="canvas">
    <section class="label">
      <svg class="label__wave-area" viewBox="0 0 588 1078" role="img" aria-label="Soft flowing blue and grey wave decoration sweeping down the left side of the label">
        <defs>
          <linearGradient id="wave-fill" x1="0" y1="0" x2="1" y2="1">
            <stop offset="0" stop-color="var(--wave-pale)" stop-opacity="0.9"/>
            <stop offset="0.6" stop-color="var(--wave-blue)" stop-opacity="0.55"/>
            <stop offset="1" stop-color="var(--wave-pale)" stop-opacity="0.3"/>
          </linearGradient>
        </defs>
        <path d="M170 0 C 60 260, 20 640, 420 1078 L 0 1078 L 0 0 Z" fill="url(#wave-fill)" opacity="0.55"/>
      </svg>

      <div class="brand-box">
        <div class="brand-box__frame">
          <h1 class="brand-name">TOLVANE</h1>
        </div>
      </div>

      <h2 class="product-title">
        <span class="product-title__line product-title__line--first">Fantastic</span>
        <span class="product-title__line product-title__line--second">Deodorant</span>
        <span class="product-title__joiner">with</span>
        <span class="product-title__line product-title__line--range">New Range</span>
      </h2>

      <div class="volume-pill">75 ML</div>
    </section>
  </main>
</body>
</html>
```